Digital Album Cover - Drifting Past Amber Harbor Lights (Piano & Cello)

HiI would like a digital album coverTitle: "Drifting Past Amber Harbor Lights (Piano & Cello)"Artist: "Rolf Dekker & The Osei Marit"

Requirements
Nice to have
• Original creativity
Should not have
• Copyrighted images

```html
<!DOCTYPE html>
<html lang="en">
<head>
<meta charset="utf-8">
<title>Drifting Past Amber Harbor Lights — Piano &amp; Cello</title>
<link rel="stylesheet" href="https://fonts.googleapis.com/css2?family=Oswald:wght@500&family=Roboto+Condensed:wght@400&display=swap">
<style>
  :root {
    --ink: #000000;
    --paper: #ffffff;
    --blush: #ffbfa6;
    --night-top: #1b3349;
    --night-mid: #2b5069;
    --cloud: #d8978c;
  }
  html, body {
    margin: 0;
    padding: 0;
    overflow: hidden;
    background: var(--ink);
  }
  .cover {
    position: relative;
    width: 1200px;
    height: 1200px;
    background: var(--ink);
    overflow: hidden;
  }
  .tab {
    position: absolute;
    left: 480px;
    width: 240px;
    background: var(--paper);
  }
  .tab--top { top: 0; height: 13px; }
  .tab--bottom { bottom: 0; height: 44px; }

  .title {
    position: absolute;
    left: 230px;
    top: 84px;
    margin: 0;
    font-family: "Oswald", "Arial Narrow", sans-serif;
    font-weight: 500;
    font-size: 68px;
    line-height: 73px;
    letter-spacing: 1px;
    color: var(--blush);
    text-transform: uppercase;
  }
  .title__line { display: block; white-space: nowrap; }
  .edition {
    font-family: "Roboto Condensed", "Arial Narrow", sans-serif;
    font-weight: 400;
    font-size: 40px;
    letter-spacing: 1.5px;
    color: var(--paper);
    margin-left: 22px;
  }

  .artwork {
    position: absolute;
    left: 229px;
    top: 246px;
    width: 741px;
    height: 743px;
    background: linear-gradient(180deg, var(--night-top) 0%, var(--night-mid) 55%, var(--cloud) 82%, #8a7a78 100%);
  }

  .artist {
    position: absolute;
    left: 230px;
    top: 1019px;
    margin: 0;
    font-family: "Roboto Condensed", "Arial Narrow", sans-serif;
    font-weight: 400;
    font-size: 48px;
    line-height: 56px;
    letter-spacing: 1.5px;
    color: var(--paper);
    text-transform: uppercase;
    white-space: nowrap;
  }
</style>
</head>
<body>
  <main class="cover">
    <div class="tab tab--top"></div>

    <h1 class="title">
      <span class="title__line">Drifting Past Amber</span>
      <span class="title__line">Harbor Lights<span class="edition">PIANO &amp; CELLO</span></span>
    </h1>

    <div class="artwork" role="img" aria-label="Cover artwork: dusk sky fading from deep blue to soft pink"></div>

    <p class="artist">Rolf Dekker &amp; The Osei Marit</p>

    <div class="tab tab--bottom"></div>
  </main>
</body>
</html>
```